K9 Orbit needs a business card designed

We need a business card designed for K9 Orbit, an expansion of K9 Technics Pty Ltd (www.k9technics.com.au)

We provide high quality professional services for the Australian space industry. Our clients include the Southern Stellar Bureau and companies working in the space industry. We identify people with space related skills both locally and internationally who are then contracted by clients to create products and support space launch activities.

Colours to be used:
- Navy blue #000080
- Rocket metallic #8A7F8D
- Platinum #E5E4E2
- Black #000000
- White #FFFFFF

*Front of the card*
I have attached our K9 Orbit logo, which needs to be the main item on the card. The 'Space' text should be placed to the right of the 'K9' part rather than below, similar to the attached K9 Technics card, which this card should match.

If subtext is included, however, it should read ‘Labour Hire • Consultancy • Project Delivery’ rather than the ‘Design • Build • Test • Maintain’ of the K9 Technics card.

A black background (rather than blue background in the K9 Technics card) might be good, with a white pattern as in the K9 Technics card. If colour is used, the logo should be in its standard colours (as provided for the K9 Orbit logo).

*Back of the card*
Include a smaller K9 Orbit logo on the back.

We need the following details for K9 Orbit personnel (as a template for entry):
- Name
- Company Position
- Mobile Number
- Email
- Office Address
- Include the K9 Orbit website: www.k9orbit.com.au

Overall, we'd like to see a design that communicates the adventure of space, professional integrity, and customer service. We look forward to seeing what you can come up with.

Target Market(s)

We provide high quality professional services for the Australian space industry. Our clients include the Southern Stellar Bureau and companies working in the space industry.

Contact Information for Business Card

- Name
- Company Position
- Mobile Number
- Email
- Office Address

Requirements
Must have
• See project description.

```html
<!DOCTYPE html>
<html lang="en">
<head>
<meta charset="utf-8">
<title>K9 Orbit Business Card</title>
<link href="https://fonts.googleapis.com/css2?family=Lato:wght@400;700&family=Montserrat:wght@800&display=swap" rel="stylesheet">
<style>
  :root {
    --navy: #1f1a7a;
    --metal: #8a7f8d;
    --platinum: #e5e4e2;
    --black: #000000;
    --white: #ffffff;
    --stage: #d3d4d0;
  }
  html, body {
    margin: 0;
    padding: 0;
    width: 1200px;
    height: 801px;
    overflow: hidden;
    background: var(--stage);
  }
  .canvas {
    position: relative;
    width: 1200px;
    height: 801px;
  }
  .card {
    position: absolute;
    top: 246px;
    width: 540px;
    height: 309px;
    box-sizing: border-box;
    box-shadow: 0 6px 18px rgba(0,0,0,0.18);
    overflow: hidden;
  }
  .card--back { left: 40px; background: var(--white); }
  .card--front { left: 620px; background: var(--black); }

  .wordmark {
    font-family: "Lato", sans-serif;
    font-weight: 700;
    letter-spacing: 0;
    white-space: nowrap;
    margin: 0;
  }
  .tagline {
    font-family: "Lato", sans-serif;
    font-weight: 400;
    white-space: nowrap;
    margin: 0;
  }

  /* back */
  .back-logo {
    position: absolute;
    top: 36px;
    right: 44px;
    text-align: left;
  }
  .back-logo .wordmark { font-size: 30px; color: var(--navy); }
  .back-logo .tagline { font-size: 10px; color: var(--navy); margin-top: 6px; letter-spacing: 0.02em; }
  .rule {
    position: absolute;
    left: 30px;
    right: 30px;
    height: 1px;
    background: var(--metal);
  }
  .rule--main { top: 120px; }
  .person {
    position: absolute;
    left: 30px;
    top: 150px;
  }
  .person__name {
    font-family: "Montserrat", sans-serif;
    font-weight: 800;
    font-size: 22px;
    color: var(--navy);
    margin: 0;
    letter-spacing: 0.01em;
  }
  .person__role {
    font-family: "Lato", sans-serif;
    font-size: 15px;
    color: var(--metal);
    margin: 4px 0 0;
  }
  .rule--contact { top: 218px; right: 290px; }
  .contacts {
    position: absolute;
    left: 30px;
    top: 228px;
    list-style: none;
    margin: 0;
    padding: 0;
    font-family: "Lato", sans-serif;
    font-size: 14px;
    color: var(--metal);
  }
  .contacts li {
    display: flex;
    align-items: center;
    gap: 10px;
    height: 22px;
  }
  .contacts .web { color: var(--navy); }
  .contacts svg { width: 14px; height: 14px; flex: none; }
  .address {
    position: absolute;
    right: 40px;
    top: 150px;
    font-family: "Lato", sans-serif;
    font-size: 15px;
    line-height: 1.5;
    color: var(--metal);
    font-style: normal;
  }

  /* front */
  .front-arcs { position: absolute; inset: 0; }
  .front-logo {
    position: absolute;
    left: 0;
    right: 0;
    top: 112px;
    text-align: center;
  }
  .front-logo .wordmark { font-size: 46px; color: var(--white); }
  .front-logo .tagline { font-size: 13px; color: var(--white); margin-top: 8px; letter-spacing: 0.03em; }
</style>
</head>
<body>
<main class="canvas">

  <section class="card card--back" aria-label="Card back">
    <div class="back-logo">
      <p class="wordmark">K9 Orbit</p>
      <p class="tagline">Labour Hire • Consultancy • Project Delivery</p>
    </div>
    <div class="rule rule--main"></div>

    <div class="person">
      <h1 class="person__name">ALEX CARTER</h1>
      <p class="person__role">Founder &amp; CEO</p>
    </div>
    <div class="rule rule--contact"></div>

    <ul class="contacts">
      <li>
        <svg viewBox="0 0 14 14" aria-hidden="true"><circle cx="7" cy="7" r="7" fill="var(--navy)"/><path d="M4.5 3.5l1.6 1.6-.9 1.1a6 6 0 002.6 2.6l1.1-.9 1.6 1.6-1 1.1C6.6 10.6 3.4 7.4 3.4 4.5z" fill="#fff"/></svg>
        <span>000 5555 7777</span>
      </li>
      <li>
        <svg viewBox="0 0 14 14" aria-hidden="true"><circle cx="7" cy="7" r="7" fill="var(--navy)"/><rect x="3" y="4.5" width="8" height="5.5" fill="none" stroke="#fff" stroke-width="1"/><path d="M3 4.5l4 3 4-3" fill="none" stroke="#fff" stroke-width="1"/></svg>
        <span>info@k9orbit.com.au</span>
      </li>
      <li>
        <svg viewBox="0 0 14 14" aria-hidden="true"><circle cx="7" cy="7" r="7" fill="var(--navy)"/><circle cx="7" cy="7" r="4" fill="none" stroke="#fff" stroke-width="0.9"/><ellipse cx="7" cy="7" rx="1.8" ry="4" fill="none" stroke="#fff" stroke-width="0.9"/><path d="M3 7h8" stroke="#fff" stroke-width="0.9"/></svg>
        <span class="web">www.k9orbit.com.au</span>
      </li>
    </ul>

    <address class="address">
      1234 First Line Address<br>
      5678 Second Line Address
    </address>
  </section>

  <section class="card card--front" aria-label="Card front">
    <svg class="front-arcs" viewBox="0 0 540 309" preserveAspectRatio="none" aria-hidden="true">
      <path d="M0 0 H130 C60 60 30 180 80 309 H0 Z" fill="var(--white)"/>
      <path d="M0 0 H118 C48 64 22 182 70 309 H0 Z" fill="var(--black)"/>
      <path d="M540 0 H460 C520 70 525 200 470 309 H540 Z" fill="var(--white)"/>
      <path d="M540 0 H472 C532 72 537 198 482 309 H540 Z" fill="var(--black)"/>
    </svg>
    <div class="front-logo">
      <p class="wordmark">K9 Orbit</p>
      <p class="tagline">Labour Hire • Consultancy • Project Delivery</p>
    </div>
  </section>

</main>
</body>
</html>
```